Kanomiva business cards/stationary
Relocation Support Services
I need single sided standard sized Business Card [3.5" x 2"]
Designer's discretion
Professional
Ned Palmer
President
5-31-08 Nishimorino
Suginami-ku, Tokyo 168-0072
ned@kanomiva.com
www.kanomiva.com
Have not yet received logo files from designer. I will be using
Will upload Al format as soon as I receive from designer.
Kanomiva logo to be used

```html
<!DOCTYPE html>
<html lang="en">
<head>
<meta charset="utf-8">
<title>Kanomiva Stationery Set</title>
<link href="https://fonts.googleapis.com/css2?family=Open+Sans:wght@400;600;700&display=swap" rel="stylesheet">
<style>
  :root {
    --board: #2b2b2b;
    --board-light: #363636;
    --paper: #ffffff;
    --red: #c4161c;
    --red-dark: #8e0d12;
    --grey: #8a8a8a;
    --grey-light: #d9d9d9;
    --ink: #333333;
    --faint: #f3e6e6;
    --caption: #9a9a9a;
  }
  * { margin: 0; padding: 0; box-sizing: border-box; }
  html, body { width: 1200px; height: 338px; overflow: hidden; }
  body {
    background: radial-gradient(circle at 50% 40%, var(--board-light), var(--board));
    font-family: "Open Sans", Arial, sans-serif;
    position: relative;
  }
  .item { position: absolute; background: var(--paper); overflow: hidden; box-shadow: 0 1px 3px rgba(0,0,0,.5); }
  .caption { position: absolute; font-size: 5px; color: var(--caption); letter-spacing: .2px; white-space: nowrap; }
  .brand { position: absolute; display: flex; align-items: center; gap: 3px; }
  .brand-dot { border-radius: 50%; background: var(--red); }
  .brand-name { font-weight: 700; color: var(--red); line-height: 1; }
  .tagline { font-size: 3px; color: var(--grey); margin-top: 1px; }
  .faint-mark { position: absolute; border-radius: 50%; background: var(--faint); }
  .swoosh { position: absolute; top: 0; right: 0; }
  .contact { position: absolute; font-size: 3.2px; line-height: 1.5; color: var(--ink); }
  .contact .person { font-weight: 700; font-size: 4px; }

  /* business cards */
  .card-front { left: 34px; top: 98px; width: 92px; height: 52px; }
  .card-back { left: 34px; top: 168px; width: 92px; height: 52px; }

  /* letterheads */
  .letterhead-one { left: 158px; top: 12px; width: 219px; height: 298px; }
  .letterhead-two { left: 391px; top: 12px; width: 219px; height: 298px; }
  .letter-footer { position: absolute; left: 0; right: 0; bottom: 10px; text-align: center; font-size: 3.4px; color: var(--grey); }

  /* envelopes */
  .envelope-front { left: 629px; top: 30px; width: 230px; height: 94px; }
  .envelope-back { left: 629px; top: 150px; width: 230px; height: 94px; }

  /* flap views */
  .flap-red { left: 912px; top: 30px; width: 274px; height: 100px; background: transparent; box-shadow: none; }
  .flap-white { left: 912px; top: 150px; width: 274px; height: 140px; }
</style>
</head>
<body>

  <!-- business card front -->
  <span class="caption" style="left:34px;top:89px;">Business card front</span>
  <div class="item card-front">
    <svg class="swoosh" width="40" height="52" viewBox="0 0 40 52">
      <path d="M14 0 H40 V52 C34 30 26 12 14 0 Z" fill="var(--red)"/>
      <path d="M8 0 H14 C26 12 34 30 40 52 H38 C30 30 22 12 8 0 Z" fill="var(--grey-light)"/>
    </svg>
    <div class="brand" style="left:6px;top:6px;">
      <span class="brand-dot" style="width:6px;height:6px;"></span>
      <div><div class="brand-name" style="font-size:6px;">Kanomiva</div><div class="tagline">Relocation Support Services</div></div>
    </div>
    <div class="contact" style="left:6px;top:26px;">
      <div class="person">Ned Palmer</div>
      <div>President</div>
      <div>5-31-08 Nishimorino, Suginami-ku, Tokyo 168-0072</div>
      <div>ned@kanomiva.com · www.kanomiva.com</div>
    </div>
  </div>

  <!-- business card back -->
  <span class="caption" style="left:34px;top:159px;">Business card back</span>
  <div class="item card-back">
    <div class="faint-mark" style="left:52px;top:10px;width:34px;height:34px;"></div>
    <div class="brand" style="left:24px;top:20px;">
      <span class="brand-dot" style="width:7px;height:7px;"></span>
      <div><div class="brand-name" style="font-size:8px;">Kanomiva</div><div class="tagline">Relocation Support Services</div></div>
    </div>
  </div>

  <!-- letterhead one -->
  <div class="item letterhead-one">
    <svg class="swoosh" width="110" height="150" viewBox="0 0 110 150">
      <path d="M40 0 H110 V150 C100 80 75 30 40 0 Z" fill="var(--red)"/>
      <path d="M28 0 H40 C75 30 100 80 110 150 H106 C94 84 66 32 28 0 Z" fill="var(--grey-light)"/>
    </svg>
    <div class="brand" style="left:14px;top:14px;">
      <span class="brand-dot" style="width:9px;height:9px;"></span>
      <div><div class="brand-name" style="font-size:10px;">Kanomiva</div><div class="tagline" style="font-size:4px;">Relocation Support Services</div></div>
    </div>
    <div class="faint-mark" style="left:60px;top:100px;width:100px;height:100px;"></div>
    <div class="letter-footer">5-31-08 Nishimorino, Suginami-ku, Tokyo 168-0072 · ned@kanomiva.com · www.kanomiva.com</div>
  </div>
  <span class="caption" style="left:245px;top:316px;">Letterhead first page</span>

  <!-- letterhead two -->
  <div class="item letterhead-two">
    <svg class="swoosh" width="110" height="150" viewBox="0 0 110 150">
      <path d="M40 0 H110 V150 C100 80 75 30 40 0 Z" fill="var(--red)"/>
      <path d="M28 0 H40 C75 30 100 80 110 150 H106 C94 84 66 32 28 0 Z" fill="var(--grey-light)"/>
    </svg>
    <div class="faint-mark" style="left:60px;top:100px;width:100px;height:100px;"></div>
    <div class="letter-footer">5-31-08 Nishimorino, Suginami-ku, Tokyo 168-0072 · ned@kanomiva.com · www.kanomiva.com</div>
  </div>
  <span class="caption" style="left:475px;top:316px;">Letterhead second page</span>

  <!-- envelope front -->
  <div class="item envelope-front">
    <svg class="swoosh" width="50" height="60" viewBox="0 0 50 60">
      <path d="M18 0 H50 V60 C44 34 34 14 18 0 Z" fill="var(--red)"/>
      <path d="M12 0 H18 C34 14 44 34 50 60 H48 C40 36 28 14 12 0 Z" fill="var(--grey-light)"/>
    </svg>
    <div class="brand" style="left:10px;top:10px;">
      <span class="brand-dot" style="width:7px;height:7px;"></span>
      <div><div class="brand-name" style="font-size:7px;">Kanomiva</div><div class="tagline">Relocation Support Services</div></div>
    </div>
    <div class="contact" style="left:10px;top:28px;">
      <div>5-31-08 Nishimorino</div>
      <div>Suginami-ku, Tokyo 168-0072</div>
    </div>
    <div class="faint-mark" style="left:150px;top:30px;width:56px;height:56px;"></div>
  </div>
  <span class="caption" style="left:720px;top:128px;">Envelope front</span>

  <!-- envelope back -->
  <div class="item envelope-back">
    <div class="brand" style="left:10px;top:10px;">
      <span class="brand-dot" style="width:7px;height:7px;"></span>
      <div><div class="brand-name" style="font-size:7px;">Kanomiva</div><div class="tagline">Relocation Support Services</div></div>
    </div>
    <div class="contact" style="left:10px;top:28px;">
      <div>5-31-08 Nishimorino</div>
      <div>Suginami-ku, Tokyo 168-0072</div>
    </div>
    <div class="faint-mark" style="left:150px;top:30px;width:56px;height:56px;"></div>
  </div>
  <span class="caption" style="left:720px;top:248px;">Envelope back</span>

  <!-- flap views -->
  <div class="item flap-red">
    <svg width="274" height="100" viewBox="0 0 274 100">
      <defs>
        <linearGradient id="redFlap" x1="0" y1="0" x2="0" y2="1">
          <stop offset="0" stop-color="var(--red-dark)"/>
          <stop offset=".5" stop-color="var(--red)"/>
          <stop offset="1" stop-color="var(--red-dark)"/>
        </linearGradient>
        <linearGradient id="greyFlap" x1="0" y1="0" x2="0" y2="1">
          <stop offset="0" stop-color="#5e5e5e"/>
          <stop offset=".5" stop-color="#a8a8a8"/>
          <stop offset="1" stop-color="#5e5e5e"/>
        </linearGradient>
      </defs>
      <path d="M0 4 Q0 0 6 0 H268 Q274 0 274 4 V26 Q137 50 0 26 Z" fill="url(#redFlap)"/>
      <path d="M0 60 Q137 36 274 60 V78 Q137 100 0 78 Z" fill="url(#greyFlap)"/>
      <rect x="0" y="80" width="274" height="20" fill="var(--paper)"/>
    </svg>
  </div>
  <div class="item flap-white">
    <svg width="274" height="140" viewBox="0 0 274 140">
      <path d="M0 0 L137 56 L274 0" fill="none" stroke="var(--grey-light)" stroke-width="1"/>
      <path d="M0 140 L110 70 M274 140 L164 70" fill="none" stroke="#eeeeee" stroke-width="1"/>
    </svg>
  </div>
  <span class="caption" style="left:1010px;top:296px;">Envelope flap view</span>

</body>
</html>
```